【画像サイズ】※MZSより抜粋
表紙ファイルの理想的な採寸は2,560×1,600ピクセルです。
注:画像の寸法は1,000×625ピクセル以上であることが必要です。
画像の最大の寸法は10,000×10,000ピクセルです。

【タイトル】
家族向け専任相談員がすすめる日々の工夫
ドキドキ平気!まあるい毎日の育ち術

サブキャッチ
心理学×四柱推命メソッド
我が子を上手に愛したいあなたへ

【著者】
ひだまりファミリーケア協会 もりした かなえ

【本の内容】
子どもを怒って、自分を責めてしまうお母様向けです。
子育ての悩みを、育児書やインターネット情報では効果がなかったり
どちらにも相談できなかったりする現状。
心理学×四柱推命メソッドで、お母様とお子様だけの簡単な解決方法を
やさしくお伝えします。
子どもと過ごすのが楽しくなり、母子ともに満たされ笑顔・Happyな暮らしを実現します。

※本文を参考資料として添付いたします。

【デザイン要望】
タイトル、サブキャッチと合わせて
読者様特典プレゼントのアピールもしたいです。

読者様特典として、イラストでやさしくわかりやすい!四柱推命電子書籍プレゼント

特にイメージにこだわりはありませんので、
自由な発想でのデザインご応募を楽しみにしております。

※次点、次々点の方への参加報酬を設定いたしました。

※その他、必要な情報がありましたら、お問い合わせください。
どうぞ、よろしくお願いいたします。

依頼のジャンルは、子育て・母親向け・育児法・心理学・学び・カウンセリング です。
カテゴリーに近いものがなく、ひとまず、資格・習い事としております。

優しい色使いと、見やすいタイトル、まとまり感でこちらに決定いたしました。

たくさんの素晴らしい商品にに感動しました。本当にありがとうございました。どちらも選びたくて本当に、迷いに迷いました。

```html
<!DOCTYPE html>
<html lang="ja">
<head>
<meta charset="UTF-8">
<title>ドキドキ平気!まあるい毎日の育ち術</title>
<link rel="stylesheet" href="https://fonts.googleapis.com/css2?family=M+PLUS+Rounded+1c:wght@400;500;700;800&display=swap">
<style>
  :root {
    --bg-pink: #f6d2db;
    --bg-pink-light: #f9dee5;
    --title-pink: #e2457e;
    --accent-pink: #e5578a;
    --highlight-yellow: #f5eb8c;
    --tag-orange: #f19a3e;
    --ink: #4a3a3c;
    --ink-soft: #7a6a6c;
    --white: #ffffff;
    --photo-light: #fbf4f2;
    --photo-skin: #f0d6c8;
    --photo-warm: #e9c2b2;
  }
  * { margin: 0; padding: 0; box-sizing: border-box; }
  html, body { width: 750px; height: 1200px; overflow: hidden; }
  body {
    position: relative;
    background: linear-gradient(180deg, var(--bg-pink-light) 0%, var(--bg-pink) 100%);
    font-family: "M PLUS Rounded 1c", sans-serif;
    color: var(--ink);
  }
  .lead {
    position: absolute; top: 30px; left: 14px;
    display: flex; align-items: center; gap: 18px;
  }
  .lead-tag {
    background: var(--tag-orange); color: var(--white);
    font-size: 31px; font-weight: 700;
    padding: 4px 16px; border-radius: 8px;
  }
  .lead-text { font-size: 33px; font-weight: 700; color: var(--ink); letter-spacing: 0.02em; }

  .title { position: absolute; left: 14px; top: 92px; }
  .title-line {
    display: block; position: relative;
    font-size: 100px; font-weight: 800; line-height: 1;
    color: var(--title-pink); letter-spacing: 0.04em;
    margin-bottom: 8px;
  }
  .title-line::after {
    content: ""; position: absolute; left: 0; right: -10px; bottom: -6px;
    height: 22px; background: var(--highlight-yellow); z-index: -1; border-radius: 4px;
  }
  .title-line span { position: relative; }
  .title-line { z-index: 1; isolation: isolate; }

  .side-note {
    position: absolute; font-size: 30px; font-weight: 700;
    color: var(--ink-soft); letter-spacing: 0.03em;
  }
  .side-note b { color: var(--title-pink); font-weight: 800; }
  .side-note--one { left: 455px; top: 140px; }
  .side-note--two { left: 470px; top: 236px; }

  .photo {
    position: absolute; left: 0; top: 412px; width: 750px; height: 560px;
    background:
      radial-gradient(ellipse 55% 60% at 35% 60%, var(--photo-skin) 0%, transparent 70%),
      radial-gradient(ellipse 40% 30% at 30% 20%, var(--photo-warm) 0%, transparent 75%),
      linear-gradient(180deg, var(--photo-light), #f6e6e6);
    -webkit-mask-image: linear-gradient(180deg, transparent 0, #000 40px, #000 92%, transparent 100%);
            mask-image: linear-gradient(180deg, transparent 0, #000 40px, #000 92%, transparent 100%);
  }
  .method-box {
    position: absolute; left: 425px; top: 462px; width: 240px; height: 96px;
    background: var(--white); border-radius: 14px;
    display: flex; align-items: center; justify-content: center; text-align: center;
    font-size: 28px; font-weight: 700; line-height: 1.3; color: var(--ink);
  }
  .message {
    position: absolute; right: 70px; top: 612px; text-align: right;
    font-size: 30px; font-weight: 500; line-height: 1.65; color: var(--ink);
  }

  .bonus { position: absolute; left: 0; top: 965px; width: 750px; height: 135px; }
  .bonus-badge {
    position: absolute; left: 22px; top: 0; width: 150px; height: 135px;
    border-radius: 50%; background: var(--tag-orange); color: var(--white);
    display: flex; align-items: center; justify-content: center; text-align: center;
    font-size: 31px; font-weight: 700; line-height: 1.3; z-index: 2;
  }
  .bonus-box {
    position: absolute; left: 160px; top: 22px; width: 578px; height: 100px;
    background: var(--white); border: 3px solid var(--accent-pink); border-radius: 14px;
    display: flex; flex-direction: column; justify-content: center; padding-left: 34px;
  }
  .bonus-lead { font-size: 24px; font-weight: 700; color: var(--ink); }
  .bonus-main { font-size: 34px; font-weight: 800; color: var(--accent-pink); letter-spacing: 0.04em; }

  .author {
    position: absolute; right: 28px; top: 1110px; text-align: right;
    font-size: 27px; font-weight: 700; line-height: 1.55; color: var(--ink);
  }
</style>
</head>
<body>
  <header class="lead">
    <span class="lead-tag">家族向け専任</span>
    <span class="lead-text">相談員がすすめる日々の工夫</span>
  </header>

  <h1 class="title">
    <span class="title-line"><span>まあるい</span></span>
    <span class="title-line"><span>毎日の</span></span>
    <span class="title-line"><span>育ち術</span></span>
  </h1>
  <p class="side-note side-note--one">ドキドキ<b>平気!</b></p>
  <p class="side-note side-note--two">どんな自分も<b>ok!</b></p>

  <div class="photo" role="img" aria-label="赤ちゃんの小さな手をやさしく握る母親の手の写真"></div>
  <div class="method-box">心理学×四柱推命<br>メソッド</div>
  <p class="message">我が子を<br>上手に愛したい<br>あなたへ</p>

  <section class="bonus">
    <div class="bonus-badge">読者様<br>特典</div>
    <div class="bonus-box">
      <p class="bonus-lead">イラストでやさしくわかりやすい!</p>
      <p class="bonus-main">四柱推命電子書籍プレゼント</p>
    </div>
  </section>

  <footer class="author">
    <p>ひだまりファミリーケア協会</p>
    <p>もりした かなえ</p>
  </footer>
</body>
</html>
```